A5 Flyer Design Double Sided for a Onsite Technology company that comes to you

*** Updated Breif now ***

We made a decission that we would like a double sided A5 Flyer that is for Technology only, we will load up another for Telco later on.

Some ideas below for what we after

We want to make sure the flyer is nice looking, Attached is current business card design. I like to contuine with that flow.

Details to have on there are, Our Phone Number 02 4862 1594, our website: quonrift.com.au and our ABN number

I want to not have pricing on this more a direction that we the Computer Repair Store that comes to you.

listing our services we provide.
Updates

have updated the breif

Target Market(s)

Home, Retirment Villages and Small Business's

Requirements
Should not have
• Bright Colours

```html
<!DOCTYPE html>
<html lang="en">
<head>
<meta charset="utf-8">
<title>Quonrift Flyer</title>
<link href="https://fonts.googleapis.com/css2?family=Outfit:wght@500;600;700&family=Montserrat:wght@400;500;600&display=swap" rel="stylesheet">
<style>
:root{
  --navy:#04152a;
  --navy-mid:#0a2a48;
  --sky:#2ba3d8;
  --sky-soft:#46a6d2;
  --pale:#cfe9f7;
  --white:#ffffff;
  --ink:#24313c;
}
*{margin:0;padding:0;box-sizing:border-box}
html,body{width:1200px;height:1082px;overflow:hidden;background:var(--white)}
body{position:relative;font-family:"Montserrat",sans-serif}
.flyer{position:absolute;top:175px;width:522px;height:731px;border-radius:24px;overflow:hidden;
  background:linear-gradient(160deg,var(--navy) 0%,var(--navy) 45%,#072a48 75%,var(--navy-mid) 100%)}
.flyer--front{left:64px}
.flyer--back{left:612px}
.decor{position:absolute;inset:0;width:100%;height:100%}
.brand{position:absolute;left:49px;top:29px;display:flex;align-items:center;gap:8px;color:var(--white);
  font-weight:600;font-size:15px;letter-spacing:3px}
.brand-dot{width:34px;height:34px;border-radius:50%;background:var(--white)}
.headline{position:absolute;left:49px;font-family:"Outfit",sans-serif;font-weight:700;color:var(--sky);line-height:1;letter-spacing:-1px}
.flyer--front .headline{top:98px;font-size:48px}
.lede{position:absolute;left:52px;top:148px;color:var(--white);font-size:17.5px;line-height:22px;font-weight:500}
.banner{position:absolute;left:18px;top:211px;width:347px;height:55px;border-radius:10px;background:var(--sky-soft);
  color:var(--white);font-weight:600;font-size:11px;line-height:15.5px;padding:12px 0 0 28px}
.services{position:absolute;left:40px;top:266px;width:300px;height:332px;background:var(--white);
  clip-path:polygon(0 0,100% 0,100% 66%,50% 100%,0 100%);border-radius:0 0 0 18px;overflow:hidden}
.services-ring{position:absolute;left:-45px;top:243px;width:130px;height:130px;border-radius:50%;border:22px solid var(--pale)}
.services h2{position:absolute;left:24px;top:22px;font-family:"Outfit",sans-serif;font-weight:600;font-size:22px;line-height:26px;color:var(--ink)}
.services ul{position:absolute;left:24px;top:96px;list-style:none}
.services li{display:flex;align-items:center;gap:8px;height:23px;font-size:12.3px;font-weight:500;color:var(--ink);white-space:nowrap}
.tick{width:12px;height:12px;flex:none}
.photo{position:absolute;left:290px;top:250px;width:232px;height:481px;
  background:radial-gradient(ellipse at 60% 30%,#3f86d8 0%,#2f63a8 30%,rgba(90,110,90,.55) 60%,rgba(150,120,80,.4) 80%,transparent 100%)}
.cta{position:absolute;left:45px;top:618px;color:var(--white)}
.cta h3{font-family:"Outfit",sans-serif;font-weight:700;font-size:23px;letter-spacing:-.5px}
.phone{display:flex;align-items:center;gap:4px;margin-top:2px;font-size:10.5px}
.phone svg{width:11px;height:11px}
.details{margin-top:3px;font-size:9.5px;opacity:.9}
.flyer--back .headline{top:108px;font-size:43px}
.sub-headline{position:absolute;left:49px;top:150px;font-family:"Outfit",sans-serif;font-weight:700;font-size:25px;color:var(--sky);letter-spacing:-.5px}
.tagline{position:absolute;left:49px;top:200px;color:var(--white);font-size:17px;line-height:24px}
.audience{position:absolute;top:305px;width:198px;height:215px}
.audience--home{left:50px}
.audience--business{left:276px}
.audience-card{position:absolute;inset:0;background:var(--white);border-radius:12px;overflow:hidden;
  clip-path:polygon(0 0,100% 0,100% 64%,54% 100%,0 100%)}
.audience-ring{position:absolute;left:-38px;top:152px;width:98px;height:98px;border-radius:50%;border:16px solid var(--pale)}
.audience-tab{position:absolute;left:25px;top:-12px;width:150px;height:24px;border-radius:9px;background:var(--sky-soft);
  color:var(--white);font-family:"Outfit",sans-serif;font-weight:600;font-size:13px;text-align:center;line-height:24px}
.audience h4{position:absolute;left:16px;top:24px;font-family:"Outfit",sans-serif;font-weight:600;font-size:20px;color:var(--ink)}
.audience ul{position:absolute;left:15px;top:64px;list-style:none}
.audience li{display:flex;align-items:center;gap:6px;height:17.5px;font-size:9.3px;font-weight:500;color:var(--ink);white-space:nowrap}
.audience .tick{width:9px;height:9px}
.promise{position:absolute;left:31px;top:134px;font-family:"Outfit",sans-serif;font-weight:700;font-size:19px;color:var(--sky);letter-spacing:-.3px}
.note{position:absolute;left:50px;top:533px;font-size:8.6px;font-style:italic;color:var(--white)}
.wifi-art{position:absolute;left:266px;top:500px;width:230px;height:186px;border-radius:40% 40% 20% 20%;
  background:radial-gradient(ellipse at 50% 60%,#3b7fe0 0%,#2a63c4 40%,rgba(30,70,150,.4) 70%,transparent 100%)}
</style>
</head>
<body>

<section class="flyer flyer--front">
  <svg class="decor" viewBox="0 0 522 731" aria-hidden="true">
    <circle cx="520" cy="-20" r="230" fill="#0f4f74" opacity=".7"/>
    <circle cx="530" cy="-30" r="175" fill="#1a6d95" opacity=".55"/>
    <polygon points="0,698 522,731 0,731" fill="#46a0cc"/>
  </svg>
  <div class="brand"><span class="brand-dot"></span>QUONRIFT</div>
  <h1 class="headline">Tech Help</h1>
  <p class="lede">That Comes To<br>Your Home Or Office!</p>
  <div class="photo" role="img" aria-label="Happy man on an armchair with a laptop, in front of a large blue Wi-Fi symbol"></div>
  <div class="banner">No Need To Leave Your Home Or Office<br>We’ll Take Care Of Everything Right Where You Are</div>
  <div class="services">
    <div class="services-ring"></div>
    <h2>Services We<br>Can Provide:</h2>
    <ul>
      <li><svg class="tick" viewBox="0 0 12 12"><path d="M1 6.5l3.5 3L11 2.5" fill="none" stroke="#2ba3d8" stroke-width="1.8"/></svg>Onsite Home and/or Office Visits</li>
      <li><svg class="tick" viewBox="0 0 12 12"><path d="M1 6.5l3.5 3L11 2.5" fill="none" stroke="#2ba3d8" stroke-width="1.8"/></svg>Data Backup &amp; Cyber Security</li>
      <li><svg class="tick" viewBox="0 0 12 12"><path d="M1 6.5l3.5 3L11 2.5" fill="none" stroke="#2ba3d8" stroke-width="1.8"/></svg>Smart Home &amp; Office Technology</li>
      <li><svg class="tick" viewBox="0 0 12 12"><path d="M1 6.5l3.5 3L11 2.5" fill="none" stroke="#2ba3d8" stroke-width="1.8"/></svg>Wi-Fi Installation &amp; Troubleshooting</li>
      <li><svg class="tick" viewBox="0 0 12 12"><path d="M1 6.5l3.5 3L11 2.5" fill="none" stroke="#2ba3d8" stroke-width="1.8"/></svg>Network Setup &amp; Optimisation</li>
      <li><svg class="tick" viewBox="0 0 12 12"><path d="M1 6.5l3.5 3L11 2.5" fill="none" stroke="#2ba3d8" stroke-width="1.8"/></svg>Supply of New Computer &amp; Hardware</li>
    </ul>
  </div>
  <div class="cta">
    <h3>Call us today</h3>
    <p class="phone"><svg viewBox="0 0 12 12"><circle cx="6" cy="6" r="6" fill="#fff"/><path d="M4 3.2l1 1.4-.6.8c.4.8 1 1.4 1.8 1.8l.8-.6 1.4 1-.5 1.1C5.8 8.6 3.4 6.2 3 4z" fill="#04152a"/></svg>02 4862 1594</p>
    <p class="details">quonrift.com.au</p>
  </div>
</section>

<section class="flyer flyer--back">
  <svg class="decor" viewBox="0 0 522 731" aria-hidden="true">
    <circle cx="625" cy="370" r="195" fill="none" stroke="#2ba8e0" stroke-width="34"/>
    <polygon points="0,698 522,731 0,731" fill="#46a0cc"/>
  </svg>
  <div class="brand"><span class="brand-dot"></span>QUONRIFT</div>
  <h1 class="headline">Computer Repairs</h1>
  <p class="sub-headline">That Come To You</p>
  <p class="tagline">Local, friendly tech support,<br>right where you are</p>
  <div class="audience audience--home">
    <div class="audience-card">
      <div class="audience-ring"></div>
      <h4>Home</h4>
      <ul>
        <li><svg class="tick" viewBox="0 0 12 12"><path d="M1 6.5l3.5 3L11 2.5" fill="none" stroke="#2ba3d8" stroke-width="1.8"/></svg>Homes &amp; retirement villages</li>
        <li><svg class="tick" viewBox="0 0 12 12"><path d="M1 6.5l3.5 3L11 2.5" fill="none" stroke="#2ba3d8" stroke-width="1.8"/></svg>PC, laptop &amp; printer repairs</li>
        <li><svg class="tick" viewBox="0 0 12 12"><path d="M1 6.5l3.5 3L11 2.5" fill="none" stroke="#2ba3d8" stroke-width="1.8"/></svg>Patient, plain-English help</li>
      </ul>
      <p class="promise">We come to you</p>
    </div>
    <div class="audience-tab">Residents</div>
  </div>
  <div class="audience audience--business">
    <div class="audience-card">
      <div class="audience-ring"></div>
      <h4>Business</h4>
      <ul>
        <li><svg class="tick" viewBox="0 0 12 12"><path d="M1 6.5l3.5 3L11 2.5" fill="none" stroke="#2ba3d8" stroke-width="1.8"/></svg>Small business IT support</li>
        <li><svg class="tick" viewBox="0 0 12 12"><path d="M1 6.5l3.5 3L11 2.5" fill="none" stroke="#2ba3d8" stroke-width="1.8"/></svg>Networks, backup &amp; security</li>
        <li><svg class="tick" viewBox="0 0 12 12"><path d="M1 6.5l3.5 3L11 2.5" fill="none" stroke="#2ba3d8" stroke-width="1.8"/></svg>New hardware supplied</li>
      </ul>
      <p class="promise">Onsite visits</p>
    </div>
    <div class="audience-tab">Small Business</div>
  </div>
  <p class="note">*Your local computer repair store, on the road.</p>
  <div class="wifi-art" role="img" aria-label="Glossy blue 3D Wi-Fi signal symbol"></div>
  <div class="cta">
    <h3>Call us today</h3>
    <p class="phone"><svg viewBox="0 0 12 12"><circle cx="6" cy="6" r="6" fill="#fff"/><path d="M4 3.2l1 1.4-.6.8c.4.8 1 1.4 1.8 1.8l.8-.6 1.4 1-.5 1.1C5.8 8.6 3.4 6.2 3 4z" fill="#04152a"/></svg>02 4862 1594</p>
    <p class="details">quonrift.com.au &nbsp;·&nbsp; ABN 12 345 678 901</p>
  </div>
</section>

</body>
</html>
```